Social Search engine to end child poverty

Velquor.org is a search engine based in Houston, that donates 50% or more of its profits to nonprofit organizations that focus on ending child poverty. We consider itself a social business, claims to support full financial transparency,protect the privacy of its users;

Velquor shows advertisements next to its search results, and is paid by partners every time a user is directed to an advertiser via a sponsored link.
We are committed to becoming a privacy friendly search engine. Searches will be encrypted, not stored permanently, and data will not not sold to third party advertisers.
Like www.parvink.org Every search done by website visitor will generate a TUPRAK that will be stored in his wallet. Then the visitor can donate these TUPRAKS to The idea behind is evry donation will put a SMILE back on a child face

The search engine will partner with foundations/associations/NGOs that will be able to propose crowdfunding campaigns on the landing page

The beta test will be done with african children. So the landing page should show faces of happiness, joy, children

Please find attached inspirational ideas in the PDF file

Target Market(s)

NGO, Foundation, association, donators based in USA

Industry/Entity Type

Charity

Number of Pages Required

5+ page

Colors
33a6d7
fbed22
f04a50
a54499
f78d1f
add136

Requirements
Must have
• Landing page
• 0- Number of TUPRAKS collected worlwide/number of projects funded
• 1- explaining how it works and
• 2- samples of fundable projects
• 3- Become partner
• Search results
• 1- Sponsored results should be differentiated
• 2- The search page should advertise initiative pr people that acts in the world to end child poverty.
• 3 It should also provide quizzes with some metrics/figures on child poverty
• Under the search engine bar should be "News" "Videos

```html
<!DOCTYPE html>
<html lang="en">
<head>
<meta charset="utf-8">
<title>Velquor.org — Search the web to draw smiles</title>
<link href="https://fonts.googleapis.com/css2?family=Lato:wght@300;400;700&display=swap" rel="stylesheet">
<style>
:root{
  --yellow:#fbe122;
  --ink:#2f2f2f;
  --body:#5d5d5d;
  --muted:#8a8a8a;
  --dark:#333333;
  --soft:#f7f7f7;
  --white:#ffffff;
  --faint:#f1f1f1;
  --blue:#33a6d7;
}
*{box-sizing:border-box;margin:0;padding:0}
html,body{width:1200px;height:4269px;overflow:hidden}
body{font-family:'Lato',sans-serif;color:var(--ink);background:var(--white);position:relative}
.abs{position:absolute}

/* hero */
.hero{position:absolute;left:0;top:0;width:1200px;height:632px;
  background:radial-gradient(ellipse at 50% 45%,#6a5a4e 0%,#4a3f38 45%,#2f2925 100%)}
.hero-photo{position:absolute;inset:0}
.wallet{position:absolute;left:953px;top:30px;width:78px;height:28px;border-radius:14px;background:var(--white);
  display:flex;align-items:center;justify-content:center;gap:9px;font-size:13px;color:var(--ink)}
.wallet .dot{width:16px;height:16px;border-radius:50%;background:var(--yellow)}
.menu{position:absolute;left:1058px;top:32px;width:26px}
.menu span{display:block;height:3px;background:var(--white);margin-bottom:6px;border-radius:1px}
.brand{position:absolute;left:0;width:1200px;top:172px;text-align:center;font-size:32px;font-weight:700;color:var(--white)}
.search{position:absolute;left:301px;top:252px;width:598px;height:62px;border-radius:31px;background:var(--white);
  display:flex;align-items:center;padding:0 40px 0 42px;justify-content:space-between}
.search span{font-size:16px;color:var(--body)}
.counter{position:absolute;left:0;width:1200px;text-align:center}
.counter .num{color:var(--yellow);font-weight:700}
.hero .num{font-size:44px;top:358px;position:absolute;width:100%}
.hero .cap{font-size:20px;color:var(--white);top:422px;position:absolute;width:100%}
.circle-btn{position:absolute;width:52px;height:52px;border-radius:50%;display:flex;align-items:center;justify-content:center}

/* how it works */
.section-title{position:absolute;left:0;width:1200px;text-align:center;font-size:43px;font-weight:400;color:var(--ink)}
.section-title b{color:var(--yellow);font-weight:400}
.step-num{position:absolute;font-size:220px;font-weight:700;color:var(--faint);line-height:1}
.step h3{position:absolute;font-size:33px;font-weight:400;color:var(--ink);white-space:nowrap}
.step .rule{position:absolute;width:66px;height:3px;background:var(--yellow)}
.step p{position:absolute;font-size:17px;line-height:26.5px;color:var(--body);font-weight:400}
.art{position:absolute;border-radius:24px}

/* projects */
.projects{position:absolute;left:0;top:2562px;width:1200px;height:1302px;background:var(--soft)}
.sub{position:absolute;left:0;width:1200px;text-align:center;font-size:21px;color:var(--body)}
.card{position:absolute;width:292px;height:376px;background:var(--white);box-shadow:0 2px 8px rgba(0,0,0,.05)}
.card .status{height:209px;background:var(--dark);display:flex;align-items:center;justify-content:center;
  color:var(--yellow);font-size:19px}
.card .head{position:absolute;left:20px;right:20px;top:226px;display:flex;justify-content:space-between;font-size:25px}
.card .head .amt{color:var(--yellow)}
.card p{position:absolute;left:21px;right:30px;top:270px;font-size:13px;line-height:21px;color:var(--body)}
.card .bar{position:absolute;left:21px;right:21px;top:327px;height:8px;border-radius:4px;background:#f0f0f0}
.card .bar i{display:block;width:87%;height:100%;border-radius:4px;background:var(--yellow)}
.card .pct{position:absolute;right:20px;top:344px;font-size:9px;color:var(--muted)}

/* partner */
.partner{position:absolute;left:0;top:3864px;width:1200px;height:405px;background:var(--dark);color:var(--white)}
.partner .back{position:absolute;right:114px;top:38px;font-size:16px}
.partner h2{position:absolute;width:100%;text-align:center;top:76px;font-size:42px;font-weight:400}
.partner .lead{position:absolute;width:100%;text-align:center;top:138px;font-size:20px;color:#a8a8a8}
.cta{position:absolute;left:411px;top:211px;width:379px;height:61px;border-radius:31px;background:var(--yellow);
  color:var(--ink);font-size:20px;display:flex;align-items:center;justify-content:center}
.foot-line{position:absolute;left:114px;right:114px;top:353px;height:1px;background:#454545}
.legal{position:absolute;left:116px;top:368px;font-size:11px;color:#bdbdbd;display:flex;gap:16px}
.social{position:absolute;right:114px;top:368px;display:flex;gap:16px}
.social i{width:13px;height:13px;border-radius:50%;background:#bdbdbd;display:block}
</style>
</head>
<body>

<header class="hero">
  <div class="hero-photo" role="img" aria-label="Photo of smiling children reaching towards the camera, darkened"></div>
  <div class="wallet"><span class="dot"></span>12</div>
  <div class="menu"><span></span><span></span><span></span></div>
  <div class="brand">Velquor.org</div>
  <div class="search">
    <span>Search the web to draw smiles...</span>
    <svg width="26" height="26" viewBox="0 0 26 26" fill="none" stroke="#8a8a8a" stroke-width="1.8"><circle cx="11" cy="11" r="9"/><path d="M18 18l6 6"/></svg>
  </div>
  <div class="counter"><div class="num">524,568,887</div><div class="cap">Smiles drawn worldwide by Velquor users</div></div>
  <div class="circle-btn" style="left:574px;top:539px;background:var(--yellow)">
    <svg width="20" height="24" viewBox="0 0 20 24" fill="none" stroke="#2f2f2f" stroke-width="2"><path d="M10 2v19M3 14l7 7 7-7"/></svg>
  </div>
</header>

<h2 class="section-title" style="top:712px">How it works<b>?</b></h2>

<section class="step">
  <div class="step-num" style="left:70px;top:840px">1</div>
  <h3 style="left:116px;top:906px">Search The Web</h3>
  <div class="rule" style="left:116px;top:957px"></div>
  <p style="left:116px;top:982px;width:320px">Lorem ipsum dolor sit amet, consectetur adipiscing elit. Phasellus pharetra pretiu nibh et scelerisque. Duis sollicitudin leo nulla, at bibendum.</p>
  <div class="art" style="left:621px;top:853px;width:406px;height:340px;background:linear-gradient(135deg,#eaf4fb,#d5e9f6)" role="img" aria-label="Illustration of two people examining a computer screen with a magnifying glass"></div>
</section>

<section class="step">
  <div class="art" style="left:103px;top:1326px;width:502px;height:331px;background:linear-gradient(135deg,#fdf6d0,#e9f5de)" role="img" aria-label="Illustration of a cheerful group holding a Velquor.org banner with smile icons above"></div>
  <div class="step-num" style="left:716px;top:1320px">2</div>
  <h3 style="left:766px;top:1390px">Generate TUPRAKS</h3>
  <div class="rule" style="left:766px;top:1441px"></div>
  <p style="left:766px;top:1466px;width:320px">Lorem ipsum dolor sit amet, consectetur adipiscing elit. Phasellus pharetra pretiu nibh et scelerisque. Duis sollicitudin leo nulla, at bibendum.</p>
</section>

<section class="step">
  <div class="step-num" style="left:70px;top:1780px">3</div>
  <h3 style="left:116px;top:1851px">Donate TUPRAKS</h3>
  <div class="rule" style="left:116px;top:1902px;display:none"></div>
  <p style="left:116px;top:1926px;width:320px">Lorem ipsum dolor sit amet, consectetur adipiscing elit. Phasellus pharetra pretiu nibh et scelerisque. Duis sollicitudin leo nulla, at bibendum.</p>
  <div class="art" style="left:567px;top:1803px;width:507px;height:310px;background:linear-gradient(135deg,#c9ecef,#9fd8e0);border-radius:140px 160px 150px 120px" role="img" aria-label="Illustration of volunteers filling donation boxes with toys and clothes"></div>
</section>

<section class="step">
  <div class="step-num" style="left:560px;top:2190px">4</div>
  <h3 style="left:0;width:1200px;text-align:center;top:2254px">Put Smile on Child Face</h3>
  <p style="left:260px;width:680px;text-align:center;top:2330px">Lorem ipsum dolor sit amet, consectetur adipiscing elit. Phasellus pharetra pretiu nibh et scelerisque. Duis sollicitudin leo nulla, at bibendum.</p>
  <div class="circle-btn" style="left:574px;top:2468px;background:var(--dark)">
    <svg width="20" height="24" viewBox="0 0 20 24" fill="none" stroke="#fbe122" stroke-width="2"><path d="M10 2v19M3 14l7 7 7-7"/></svg>
  </div>
</section>

<section class="projects">
  <h2 class="section-title" style="top:80px;font-size:45px">Projects To Finance<b>.</b></h2>
  <div class="sub" style="top:142px">You shall finance one project or more</div>

  <article class="card" style="left:116px;top:232px"><div class="status">IN PROGRESS</div><div class="head"><span>Project Name</span><span class="amt">$5k</span></div><p>Lorem ipsum dolor sit amet, consectetur adipiscing elit.</p><div class="bar"><i></i></div><div class="pct">87% Funded</div></article>
  <article class="card" style="left:454px;top:232px"><div class="status">IN PROGRESS</div><div class="head"><span>Project Name</span><span class="amt">$5k</span></div><p>Lorem ipsum dolor sit amet, consectetur adipiscing elit.</p><div class="bar"><i></i></div><div class="pct">87% Funded</div></article>
  <article class="card" style="left:792px;top:232px"><div class="status">IN PROGRESS</div><div class="head"><span>Project Name</span><span class="amt">$5k</span></div><p>Lorem ipsum dolor sit amet, consectetur adipiscing elit.</p><div class="bar"><i></i></div><div class="pct">87% Funded</div></article>
  <article class="card" style="left:116px;top:666px"><div class="status">IN PROGRESS</div><div class="head"><span>Project Name</span><span class="amt">$5k</span></div><p>Lorem ipsum dolor sit amet, consectetur adipiscing elit.</p><div class="bar"><i></i></div><div class="pct">87% Funded</div></article>
  <article class="card" style="left:454px;top:666px"><div class="status">IN PROGRESS</div><div class="head"><span>Project Name</span><span class="amt">$5k</span></div><p>Lorem ipsum dolor sit amet, consectetur adipiscing elit.</p><div class="bar"><i></i></div><div class="pct">87% Funded</div></article>
  <article class="card" style="left:792px;top:666px"><div class="status">IN PROGRESS</div><div class="head"><span>Project Name</span><span class="amt">$5k</span></div><p>Lorem ipsum dolor sit amet, consectetur adipiscing elit.</p><div class="bar"><i></i></div><div class="pct">87% Funded</div></article>

  <div class="counter" style="top:1108px"><div class="num" style="font-size:42px;font-weight:400">12,842</div></div>
  <div class="sub" style="top:1172px">Project Funded worldwide by Velquor users</div>
</section>

<footer class="partner">
  <div class="back">Back to Search</div>
  <h2>Become a Partner</h2>
  <div class="lead">Propose crowdfunding campaigns to end child poverty</div>
  <div class="cta">Start Your Partnership</div>
  <div class="foot-line"></div>
  <div class="legal"><span>Privacy Policy</span><span>Terms of Use</span></div>
  <div class="social"><i></i><i></i><i></i></div>
</footer>

</body>
</html>
```